Training course diagram/design

A graphic/diagram for our website and brochures.

We are a training provider and run courses for people who wish to become professionally qualified clinical hypnotherapists.

The graphic needs to illustrate how our training course works at a glance. The training course is comprised of 5 x 4-day classroom based modules and one extra (6th) theory module which is distance learning. The diploma training is a 'rolling' course, so students can join at the beginning of any of the five (classroom) modules. It is important that it is clear from the image that there is not any specific order in which people must attend the modules (the modules have equal status). Attendance of all five modules (and completion of the theory module) will lead to the BQT (Brightmoor Trance Institute) Practitioner Diploma in Clinical Hypnotherapy Diploma.

The names of the classroom modules are:
Medical Hypnosis
Ericksonian Hypnosis
Hypno-psychotherapy
Solution Focused Hypnotherapy
Changework - NLP & Coaching

The 6th (theory module) is called:
The foundations of Hypnotherapy

I have uploaded our logo so you can see our colours/style. Our strapline is:
Practice-ready therapy training
Updates

Please use fonts used in the training school logo: 'Magmawave Caps Bold' and 'Avant Garde Bold'.

Target Market(s)

People who are wanting a creer change

Industry/Entity Type

Hypnotherapy

Font styles to use
Sans Serif
Other font styles liked:
• 'Magmawave Caps Bold' and 'Avant Garde Bold'.

Requirements
Must have
• an individual 'device' or symbol for each module (e.g. colour, shape, etc for each module) so that these can be used on different website pages or in literature where there might be a description of the contents of that module. Fonts that are consistent with branding and are easy to read.
Nice to have
• Something that complements or reflects the training school logo.

```html
<!DOCTYPE html>
<html lang="en">
<head>
<meta charset="utf-8">
<title>BQT Practitioner – Diploma Modules</title>
<link href="https://fonts.googleapis.com/css2?family=Exo+2:wght@500;600;700&display=swap" rel="stylesheet">
<style>
  :root {
    --teal: #1f9786;
    --teal-deep: #0b6652;
    --lime: #b8c55a;
    --ink: #111111;
    --label: #0f6e5c;
    --label-soft: #22a08c;
    --paper: #ffffff;
  }
  html, body {
    margin: 0;
    padding: 0;
    width: 1200px;
    height: 1093px;
    overflow: hidden;
    background: var(--paper);
  }
  .module-map {
    display: block;
    width: 1200px;
    height: 1093px;
    font-family: "Exo 2", sans-serif;
  }
  .hex {
    fill: none;
    stroke: url(#edge-gradient);
    stroke-width: 19;
    stroke-linejoin: miter;
  }
  .hex-core { fill: var(--paper); filter: url(#core-glow); }
  .module-title {
    font-weight: 600;
    font-size: 31px;
    fill: var(--ink);
    text-anchor: middle;
  }
  .module-type {
    font-weight: 600;
    font-size: 20px;
    fill: var(--label);
    text-anchor: middle;
  }
  .module-type--theory { fill: var(--label-soft); }
  .diploma-title {
    font-weight: 700;
    font-size: 38px;
    fill: var(--teal);
    text-anchor: middle;
  }
  .diploma-subtitle {
    font-weight: 600;
    font-size: 18px;
    fill: var(--label-soft);
    text-anchor: middle;
  }
  .school-mark { fill: var(--teal-deep); }
  .school-name {
    font-weight: 700;
    font-size: 17px;
    fill: var(--teal-deep);
  }
</style>
</head>
<body>
<svg class="module-map" viewBox="0 0 1440 1312" xmlns="http://www.w3.org/2000/svg" role="img"
     aria-label="BQT Practitioner Diploma in Clinical Hypnotherapy and its six modules">
  <defs>
    <linearGradient id="edge-gradient" x1="0" y1="0" x2="0.55" y2="0">
      <stop offset="0" stop-color="var(--lime)" style="stop-color:#b8c55a"/>
      <stop offset="1" stop-color="var(--teal)" style="stop-color:#1f9786"/>
    </linearGradient>
    <clipPath id="frame">
      <rect x="202" y="65" width="946" height="1197"/>
    </clipPath>
    <filter id="core-glow" x="-20%" y="-20%" width="140%" height="140%">
      <feGaussianBlur in="SourceAlpha" stdDeviation="9"/>
      <feComponentTransfer><feFuncA type="linear" slope="0.25"/></feComponentTransfer>
      <feComposite in2="SourceAlpha" operator="arithmetic" k2="-1" k3="1"/>
      <feFlood flood-color="#000"/>
      <feComposite in2="SourceAlpha" operator="in"/>
      <feGaussianBlur stdDeviation="10"/>
      <feComponentTransfer><feFuncA type="linear" slope="0.25"/></feComponentTransfer>
      <feComposite in2="SourceGraphic" operator="over"/>
      <feMerge><feMergeNode in="SourceGraphic"/><feMergeNode/></feMerge>
    </filter>
  </defs>

  <g class="hex-grid" clip-path="url(#frame)">
    <!-- theory module, top -->
    <polygon class="hex" points="437,243 556,38 796,38 915,243 796,440 556,440"/>
    <!-- upper left -->
    <polygon class="hex" points="70,453 189,255 429,255 548,453 429,651 189,651"/>
    <!-- upper right -->
    <polygon class="hex" points="800,453 919,255 1159,255 1278,453 1159,651 919,651"/>
    <!-- lower left -->
    <polygon class="hex" points="70,873 189,675 429,675 548,873 429,1073 189,1073"/>
    <!-- lower right -->
    <polygon class="hex" points="800,873 919,675 1159,675 1278,873 1159,1073 919,1073"/>
    <!-- bottom -->
    <polygon class="hex" points="437,1083 556,886 796,886 915,1083 796,1290 556,1290"/>
    <!-- diploma core -->
    <polygon class="hex hex-core" points="445,662 560,466 792,466 907,662 792,858 560,858"/>
    <polygon class="hex" points="445,662 560,466 792,466 907,662 792,858 560,858"/>
  </g>

  <g class="module module--theory">
    <text class="module-title" x="676" y="236">The foundations of</text>
    <text class="module-title" x="676" y="276">Hypnotherapy</text>
    <text class="module-type module-type--theory" x="676" y="335">( theory module )</text>
  </g>
  <g class="module">
    <text class="module-title" x="325" y="449">Ericksonian</text>
    <text class="module-title" x="329" y="489">Hypnosis</text>
    <text class="module-type" x="311" y="539">( classroom module )</text>
  </g>
  <g class="module">
    <text class="module-title" x="1022" y="429">Medical</text>
    <text class="module-title" x="1022" y="469">Hypnosis</text>
    <text class="module-type" x="1036" y="539">( classroom module )</text>
  </g>
  <g class="module">
    <text class="module-title" x="325" y="835">Solution Focused</text>
    <text class="module-title" x="329" y="875">Hypnotherapy</text>
    <text class="module-type" x="329" y="948">( classroom module )</text>
  </g>
  <g class="module">
    <text class="module-title" x="1036" y="835">Hypno-</text>
    <text class="module-title" x="1036" y="875">psychotherapy</text>
    <text class="module-type" x="1023" y="948">( classroom module )</text>
  </g>
  <g class="module">
    <text class="module-title" x="676" y="1019">Changework -</text>
    <text class="module-title" x="676" y="1059">NLP &amp; Coaching</text>
    <text class="module-type" x="676" y="1130">( classroom module )</text>
  </g>

  <g class="diploma">
    <text class="diploma-title" x="674" y="608">BQT Practitioner</text>
    <text class="diploma-subtitle" x="672" y="637">Diploma in Clinical Hypnotherapy</text>
    <circle class="school-mark" cx="614" cy="708" r="42"/>
    <text class="school-name" x="683" y="697">Brightmoor</text>
    <text class="school-name" x="683" y="717">Trance Institute</text>
  </g>
</svg>
</body>
</html>
```